Brochure for medical doctor

I need a brochure for a medical doctor to promote his practice. The brochure should contain his picture, business information (use letterhead from attachment), and the following text:

- Now accepting PI cases on lien!
- Same and next business day appointments available for initial visits, pre-operative clearances, and all other medical needs

- Expedited medical reports sent quickly to your office

Medical

```html
<!DOCTYPE html>
<html lang="en">
<head>
<meta charset="utf-8">
<title>Willow Creek Medical Center – Medical Reports and Doctor's Lien</title>
<link rel="stylesheet" href="https://fonts.googleapis.com/css2?family=Oswald:wght@600;700&family=Rubik:wght@600;700&family=Open+Sans:wght@400;600&display=swap">
<style>
  :root{
    --green:#00a86b;
    --blue:#0a78c2;
    --navy:#0b3160;
    --deep:#0d2a57;
    --text:#1e1e1e;
    --paper:#ffffff;
    --backdrop:#e9ecef;
  }
  *{box-sizing:border-box;margin:0;padding:0}
  html,body{width:1027px;height:1200px;overflow:hidden;background:var(--backdrop)}
  .flyer{position:relative;width:1027px;height:1200px;background:var(--paper);overflow:hidden;font-family:"Open Sans",Arial,sans-serif;color:var(--text)}

  .brand{position:absolute;left:58px;top:46px;display:flex;align-items:center;gap:18px}
  .brand-dot{width:70px;height:70px;border-radius:50%;background:var(--green)}
  .brand-name{font-family:"Oswald",Arial,sans-serif;font-weight:700;color:var(--blue);font-size:40px;line-height:1.02;text-transform:uppercase;letter-spacing:.5px}

  .name-band{position:absolute;left:0;top:160px;width:610px;height:120px}
  .name-band svg{position:absolute;inset:0}
  .doctor-name{position:absolute;left:58px;top:172px;color:#fff;font-family:"Oswald",Arial,sans-serif;font-weight:700;font-size:44px;line-height:1}
  .doctor-title{position:absolute;left:64px;top:228px;color:#fff;font-family:"Open Sans",Arial,sans-serif;font-size:30px;line-height:1}

  .portrait-arc{position:absolute;left:540px;top:0;width:487px;height:470px}
  .portrait{position:absolute;left:590px;top:20px;width:390px;height:390px;border-radius:50%;background:radial-gradient(circle at 50% 40%,#f3efe9 0%,#dfe6ee 55%,#cfd9e4 100%)}

  h2.section-title{font-family:"Rubik",Arial,sans-serif;font-weight:700;color:var(--navy)}
  .lien-title{position:absolute;left:58px;top:300px;font-size:29px;line-height:1.15}

  .lien-text{position:absolute;left:58px;top:392px;width:470px;font-size:12.3px;line-height:1.47;text-align:justify}
  .lien-text p{margin-bottom:10px}
  .blank{display:inline-block;width:150px;border-bottom:1px solid var(--text);height:12px;vertical-align:baseline}

  .ack-title{position:absolute;left:560px;top:470px;font-size:17px;line-height:1.25;width:410px}
  .ack-text{position:absolute;left:560px;top:522px;width:410px;font-size:11.6px;line-height:1.47;text-align:justify}

  .services{position:absolute;left:595px;top:905px;width:395px;height:205px;border-radius:16px;background:linear-gradient(160deg,var(--blue) 0%,#0a8ab0 55%,var(--green) 100%);color:#fff;font-family:"Rubik",Arial,sans-serif;font-weight:600}
  .service{position:absolute;display:flex;align-items:center;gap:14px}
  .service-icon{flex:none;width:50px;height:50px;border-radius:50%;background:var(--deep);border:3px solid #fff;display:flex;align-items:center;justify-content:center}
  .service-text{font-size:14px;line-height:1.3}
  .service-1{left:-22px;top:12px}
  .service-2{left:-22px;top:72px;width:400px}
  .service-3{left:-22px;top:140px}

  .contact-bar{position:absolute;left:0;bottom:0;width:1027px;height:70px;background:var(--navy);color:#fff;display:flex;align-items:center;justify-content:space-around;padding:0 40px;font-size:17px}
  .contact-item{display:flex;align-items:center;gap:10px}
  .contact-icon{width:30px;height:30px;border-radius:50%;border:2px solid #fff;display:flex;align-items:center;justify-content:center}
</style>
</head>
<body>
<main class="flyer">

  <div class="brand">
    <span class="brand-dot"></span>
    <div class="brand-name">Willow Creek<br>Medical Center</div>
  </div>

  <div class="name-band">
    <svg width="610" height="120" viewBox="0 0 610 120"><polygon points="0,0 610,0 530,120 0,120" fill="var(--blue)"/></svg>
  </div>
  <div class="doctor-name">Dr. Lorem Ipsum</div>
  <div class="doctor-title">Dolor Sir Amet</div>

  <svg class="portrait-arc" viewBox="0 0 487 470" aria-hidden="true">
    <defs>
      <linearGradient id="arcGrad" x1="1" y1="0" x2="0" y2="1">
        <stop offset="0" stop-color="var(--blue)"/>
        <stop offset="1" stop-color="var(--green)"/>
      </linearGradient>
    </defs>
    <path d="M360 130 C470 150 500 260 450 340 C390 440 230 470 120 420 C50 385 25 320 60 260 C45 330 100 400 200 415 C320 430 430 360 445 260 C455 200 420 150 360 130 Z" fill="url(#arcGrad)"/>
    <g fill="var(--blue)"><rect x="412" y="432" width="30" height="10"/><rect x="422" y="422" width="10" height="30"/></g>
    <g fill="var(--green)"><rect x="445" y="455" width="20" height="7"/><rect x="452" y="448" width="7" height="21"/></g>
  </svg>
  <div class="portrait" role="img" aria-label="Portrait photo of the doctor in a white coat with a stethoscope"></div>

  <h2 class="section-title lien-title">Medical Reports and<br>Doctor’s Lien</h2>

  <section class="lien-text">
    <p>I authorized the above doctor and or their authorized representatives to furnish my attorney, any attorney or attorneys who subsequently are either associated with the said attorney or substituted in their place, with a full report of my examination, diagnosis, treatment, prognosis, itemized bill of charges incurred, etc, in regard to the accident in which I was involved on <span class="blank"></span>, and hold the above doctor free and harmless from any liability insuch transfer of information.</p>
    <p>Out of the proceeds of the settlement and/or judgment in my claim for personal injuries, I hereby assign, set over and transfer to the above doctor such monies due and owing to him or the group for medical, chiropractic. X-rays, physical therapy, supplies and or laboratory fees rendered to me, either by reason of the above accident or otherwise. I further give to the above doctor a lien on any and all fund received by me or in my behave in association with the settlement or satisfaction of judgement arising from claims presented on my behalf.</p>
    <p>I fully understand that I am directly responsible to said doctors/group for all medical bills submitted by them for services rendered to me. I further understand that such payment is not contingent on any settlement, judgement or verdict by which I may eventually receive said fee. In the event legal action shall be brought in order to enforce this lien, then the prevailing party shall be entitled to reasonable costs and attorney fees in addiction to any judgment rendered. It is acknowledged by the undersigned that this assignment and lien is further consideration for the services rendered by the above doctor in addition to the obligation to pay for the medical services.</p>
    <p>Patient’s personal injury claim medical payments are hereby assigned and will be paid directly from the insurance company to Willow Creek Medical Center.</p>
    <p>Attorney agrees to notify the doctors immediately of the name and contacting information of any attorney substituted in his or her place.</p>
  </section>

  <h2 class="section-title ack-title">Acknowledgement of assignment and lien by attorney</h2>
  <section class="ack-text">
    <p>The undersigned being the attorney of record on his own behalf and on behalf of any other attorney or attorneys who are associated with the undersigned or who are substituted in his stead for the above patient, does hereby acknowledge receipt of a copy of the assignment and lien, and said attorney acknowledges that he/she obligates themselves to the terms of the assignment and lien in consideration for the rendering of medical services to their client by the above doctor and rendering of a report and bill to said attorney. In the event legal section shall be brought in order to enforce this lien. Then the prevailing party shall be entitled to reasonable costs and attorney fees in addiction to any judgment rendered. A photographic reproduction of this authorization may be used in place of the original. No charges of alterations of the monies billed herein will be accepted unless confirmed in writing bythe doctor. Please date, sign and return on copy as soon as possible to the above referenced medical provider of services in order that treatment can continue on the herein contained lien basis.</p>
  </section>

  <section class="services">
    <div class="service service-1">
      <span class="service-icon"><svg width="24" height="24" viewBox="0 0 24 24" fill="none" stroke="#fff" stroke-width="2"><path d="M6 2h9l4 4v16H6z"/><path d="M9 14l2 2 4-4"/></svg></span>
      <span class="service-text">Now accepting PI cases on lien!</span>
    </div>
    <div class="service service-2">
      <span class="service-icon"><svg width="24" height="24" viewBox="0 0 24 24" fill="none" stroke="#fff" stroke-width="2"><rect x="4" y="3" width="16" height="18"/><path d="M8 7h2M14 7h2M8 11h2M14 11h2M10 21v-5h4v5"/></svg></span>
      <span class="service-text">Same and next business day appointments available for initial visits, pre-operative clearances, and all other medical needs</span>
    </div>
    <div class="service service-3">
      <span class="service-icon"><svg width="24" height="24" viewBox="0 0 24 24" fill="none" stroke="#fff" stroke-width="2"><path d="M6 2h9l4 4v16H6z"/><path d="M9 10h7M9 14h7M9 18h5"/></svg></span>
      <span class="service-text">Expedited medical reports<br>sent quickly to your office</span>
    </div>
  </section>

  <footer class="contact-bar">
    <span class="contact-item"><span class="contact-icon"><svg width="14" height="16" viewBox="0 0 14 18" fill="var(--green)"><path d="M7 0C3 0 0 3 0 7c0 5 7 11 7 11s7-6 7-11c0-4-3-7-7-7zm0 10a3 3 0 110-6 3 3 0 010 6z"/></svg></span>4410 Larkspur Ave. Fairview, CA, 90000</span>
    <span class="contact-item"><span class="contact-icon"><svg width="14" height="14" viewBox="0 0 24 24" fill="var(--green)"><path d="M6.6 10.8a15 15 0 006.6 6.6l2.2-2.2a1 1 0 011-.25 11.4 11.4 0 003.6.57 1 1 0 011 1V20a1 1 0 01-1 1A17 17 0 013 4a1 1 0 011-1h3.5a1 1 0 011 1c0 1.25.2 2.45.57 3.57a1 1 0 01-.25 1z"/></svg></span>(555) 014-2231</span>
    <span class="contact-item"><span class="contact-icon"><svg width="14" height="14" viewBox="0 0 24 24" fill="var(--green)"><rect x="6" y="2" width="12" height="6"/><rect x="2" y="9" width="20" height="9" rx="2"/><rect x="6" y="15" width="12" height="7" fill="#fff"/></svg></span>(555) 014-2237</span>
  </footer>

</main>
</body>
</html>
```